Redesign Comparisson chart - make modern and effective

Use your imaginations to make a powerful distinction between KRV & other holistic modalities. There are 7 elements physical, mental, emotional, energetic, subconscious, superconscious and before and after testing.
We want it to be obvious that KRV is the only modality that works on all these elements simultaneously. We do not want to include any chakras as we want this information to be accepted by a wide range of people and belief systems.'

We want it to look simple but effective. Professional but powerful. We want KRV to stand out even of you eye just passed over i.
Updates

Hi everyone, thanks for your submissions so far. Basically what this image is meant to represent is a comparison chart between all the modalities There are 5 elements physical, mental, emotional, subconscious and superconscious. we want to reflect that KRV is the only modality that works on all these elements simultaneously. As we want the concept to be accepted and not considered woo woo, we want to steer away from chakras.

Target Market(s)

Professionals

Industry/Entity Type

Professional services

Font styles to use
Sans Serif
Other font styles liked:
• Poppins Monserratt

Colors
0094D4
00A9DD
6FCCEA
C7EBF8
E9F6FB

Requirements
Must have
• Clear/professional and clean look. Brand colours and logos. All typography and formats must be cohesive.
Nice to have
• More easy to read, different layout
Should not have
• Do not change the data just the way its presented. No chakras

```html
<!DOCTYPE html>
<html lang="en">
<head>
<meta charset="utf-8">
<title>KRV Comparison Chart</title>
<link href="https://fonts.googleapis.com/css2?family=Poppins:wght@400;500;600;700&family=Oswald:wght@300;400&display=swap" rel="stylesheet">
<style>
  :root{
    --brand:#2bb5e6;
    --ink:#222;
    --cell:#c5edfb;
    --label-soft:#b5e3f3;
    --physical:#d9555a;
    --mental:#8fcbdc;
    --emotional:#83c061;
    --energetic:#dc8434;
    --subconscious:#f2e46e;
    --superconscious:#927fb0;
    --testing:#9c6a95;
    --tick-mental:#3fc2ec;
    --tick-sub:#f5e000;
  }
  *{box-sizing:border-box;margin:0;padding:0}
  html,body{width:1200px;height:870px;overflow:hidden;background:#fff}
  body{position:relative;font-family:'Poppins',sans-serif;color:var(--ink)}

  .brand-mark{position:absolute;left:22px;top:40px;width:78px;height:78px;border-radius:50%;background:var(--brand)}
  .brand-name{position:absolute;left:112px;top:44px;font-weight:700;font-size:26px;line-height:25px;color:var(--brand)}
  .brand-name .code{display:block;font-size:30px;line-height:28px;margin-top:-4px}
  .divider{position:absolute;left:248px;top:18px;width:3px;height:116px;background:var(--brand)}
  .headline{position:absolute;left:264px;top:40px;font-weight:600;font-size:31px;letter-spacing:.2px;color:var(--brand);white-space:nowrap}
  .intro{position:absolute;left:264px;top:80px;width:920px;font-family:'Oswald',sans-serif;font-weight:300;font-size:18.5px;line-height:26px;color:#333}

  .chart{position:absolute;left:17px;top:155px;width:1165px}
  .row{display:grid;grid-template-columns:172px 132px 132px 132px 132px 167px 167px 131px;border-bottom:2px solid #fff}
  .row > div{display:flex;align-items:center;justify-content:center;background:var(--cell);border-left:2px solid #fff}
  .row > .label{justify-content:flex-start;padding-left:8px;border-left:none;color:#fff;font-size:9.4px;line-height:10px;text-transform:uppercase;background:#45bde6}
  .head > div{color:#fff;font-weight:600;font-size:13px;line-height:15px;text-align:center;height:44px;border-left:none}
  .head > .label{background:#fff}
  .h-physical{background:var(--physical)!important}
  .h-mental{background:var(--mental)!important}
  .h-emotional{background:var(--emotional)!important}
  .h-energetic{background:var(--energetic)!important}
  .h-sub{background:var(--subconscious)!important}
  .h-super{background:var(--superconscious)!important}
  .h-testing{background:var(--testing)!important}

  .group .label{background:var(--label-soft);color:#222;flex-direction:column;align-items:flex-start;justify-content:center;gap:8px;font-size:9.4px}
  .row.alt .label{background:#5dc3e6}
  .row.alt2 .label{background:#2eb7ea}
  .row.alt3 .label{background:#6fcbea}

  .featured{position:relative;z-index:1;outline:2px solid var(--brand);margin:0 -3px;padding:0 3px;background:#fff}
  .featured > div{background:#fff!important;border-left-color:#fff}
  .featured .label{color:#222;font-size:10px;gap:8px}
  .featured .dot{width:15px;height:15px;border-radius:50%;background:var(--brand)}

  .tick{width:15px;height:13px}
  .featured .tick{width:17px;height:15px}
  .c-physical{color:var(--physical)}
  .c-mental{color:var(--tick-mental)}
  .c-emotional{color:var(--emotional)}
  .c-energetic{color:var(--energetic)}
  .c-sub{color:var(--tick-sub)}
  .c-super{color:var(--superconscious)}
  .c-testing{color:var(--testing)}

  .partner{position:absolute;left:22px;top:712px;display:flex;align-items:center;gap:10px}
  .partner .dot{width:34px;height:34px;border-radius:50%;background:var(--brand)}
  .partner .name{font-weight:700;font-size:30px;color:var(--brand)}
  .site{position:absolute;left:36px;top:795px;font-weight:600;font-size:13.5px;color:var(--brand)}

  .notes{position:absolute;top:692px;display:flex;flex-direction:column;gap:12px;font-size:8.3px;line-height:11px;color:#333;text-align:justify}
  .notes h3{font-size:14px;font-weight:600;text-align:center;margin-bottom:2px}
  .notes-col{position:absolute;top:690px;height:166px;width:1px;background:#e4e4e4}
  .n1{left:285px;width:180px}
  .n2{left:506px;width:178px}
  .n3{left:726px;width:180px}
  .n4{left:958px;width:180px}
</style>
</head>
<body>
<svg width="0" height="0" style="position:absolute">
  <symbol id="tick" viewBox="0 0 20 17"><path d="M0 8 L3 6 L7 11 Q12 3 20 0 Q12 6 7.5 17 Z" fill="currentColor"/></symbol>
</svg>

<header>
  <div class="brand-mark"></div>
  <div class="brand-name"><span class="code">KRV</span>kinetic root<br>vitality</div>
  <div class="divider"></div>
  <h1 class="headline">CHOOSE KRV FOR FAST, IMMEDIATE &amp; POWERFUL RESULTS</h1>
  <p class="intro">I must experience healing on all levels I am not just a body want to learn how to heal myself,so I'm not dependent on others. I want to release all my emotional &amp; mental blocks so i can be the best version of myself.</p>
</header>

<section class="chart">
  <div class="row head">
    <div class="label"></div>
    <div class="h-physical">PHYSICAL</div><div class="h-mental">MENTAL</div><div class="h-emotional">EMOTIONAL</div><div class="h-energetic">ENERGETIC</div><div class="h-sub">SUBCONSCIOUS</div><div class="h-super">SUPERCONSCIOUS</div><div class="h-testing">BEFORE &amp;<br>AFTER TESTING</div>
  </div>
  <div class="row group" style="height:112px">
    <div class="label"><span>MASSAGE</span><span>YOGA</span><span>NATUROPATHY</span><span>AYURVEDI MEDICINE</span><span>WESTERN MEDICINE</span></div>
    <div><svg class="tick c-physical"><use href="#tick"/></svg></div><div></div><div></div><div></div><div></div><div></div><div></div>
  </div>
  <div class="row alt2" style="height:22px"><div class="label">PSYCHIC INTUITIVE</div>
    <div><svg class="tick c-physical"><use href="#tick"/></svg></div><div><svg class="tick c-mental"><use href="#tick"/></svg></div><div></div><div></div><div></div><div></div><div></div></div>
  <div class="row alt2" style="height:21px"><div class="label">FAMILY CONSTELLATION</div>
    <div><svg class="tick c-physical"><use href="#tick"/></svg></div><div><svg class="tick c-mental"><use href="#tick"/></svg></div><div></div><div><svg class="tick c-energetic"><use href="#tick"/></svg></div><div></div><div></div><div></div></div>
  <div class="row" style="height:21px"><div class="label">ACCUPUNTURE</div>
    <div><svg class="tick c-physical"><use href="#tick"/></svg></div><div></div><div></div><div><svg class="tick c-energetic"><use href="#tick"/></svg></div><div></div><div></div><div></div></div>
  <div class="row alt" style="height:20px"><div class="label">NUTRIONAL HEALING</div>
    <div><svg class="tick c-physical"><use href="#tick"/></svg></div><div></div><div></div><div></div><div></div><div></div><div><svg class="tick c-testing"><use href="#tick"/></svg></div></div>
  <div class="row alt3" style="height:22px"><div class="label">CHINESE MEDICINE</div>
    <div><svg class="tick c-physical"><use href="#tick"/></svg></div><div></div><div></div><div><svg class="tick c-energetic"><use href="#tick"/></svg></div><div></div><div></div><div><svg class="tick c-testing"><use href="#tick"/></svg></div></div>
  <div class="row alt3" style="height:21px"><div class="label">KINESIOLOGY I BOWMEN THERAPY</div>
    <div><svg class="tick c-physical"><use href="#tick"/></svg></div><div></div><div></div><div></div><div></div><div></div><div><svg class="tick c-testing"><use href="#tick"/></svg></div></div>
  <div class="row featured" style="height:26px"><div class="label">KINETIC ROOT VITALITY <span class="dot"></span></div>
    <div><svg class="tick c-physical"><use href="#tick"/></svg></div><div><svg class="tick c-mental"><use href="#tick"/></svg></div><div><svg class="tick c-emotional"><use href="#tick"/></svg></div><div><svg class="tick c-energetic"><use href="#tick"/></svg></div><div><svg class="tick c-sub"><use href="#tick"/></svg></div><div><svg class="tick c-super"><use href="#tick"/></svg></div><div><svg class="tick c-testing"><use href="#tick"/></svg></div></div>
  <div class="row alt" style="height:25px"><div class="label">EFT</div>
    <div><svg class="tick c-physical"><use href="#tick"/></svg></div><div><svg class="tick c-mental"><use href="#tick"/></svg></div><div></div><div></div><div><svg class="tick c-sub"><use href="#tick"/></svg></div><div></div><div><svg class="tick c-testing"><use href="#tick"/></svg></div></div>
  <div class="row alt" style="height:25px"><div class="label">CHIROPRACTIC</div>
    <div><svg class="tick c-physical"><use href="#tick"/></svg></div><div></div><div></div><div><svg class="tick c-energetic"><use href="#tick"/></svg></div><div><svg class="tick c-sub"><use href="#tick"/></svg></div><div></div><div><svg class="tick c-testing"><use href="#tick"/></svg></div></div>
  <div class="row" style="height:26px"><div class="label">REIKI<br>CRYSTAL HEALING</div>
    <div></div><div></div><div></div><div><svg class="tick c-energetic"><use href="#tick"/></svg></div><div></div><div></div><div></div></div>
  <div class="row alt" style="height:23px"><div class="label">ENERGY MEDICINE</div>
    <div></div><div></div><div></div><div><svg class="tick c-energetic"><use href="#tick"/></svg></div><div></div><div></div><div><svg class="tick c-testing"><use href="#tick"/></svg></div></div>
  <div class="row alt3" style="height:25px"><div class="label">THETA HEALING</div>
    <div></div><div></div><div></div><div></div><div></div><div></div><div></div></div>
  <div class="row" style="height:24px"><div class="label">PSYCHOLOGY</div>
    <div></div><div><svg class="tick c-mental"><use href="#tick"/></svg></div><div></div><div></div><div><svg class="tick c-sub"><use href="#tick"/></svg></div><div><svg class="tick c-super"><use href="#tick"/></svg></div><div></div></div>
  <div class="row alt3" style="height:24px"><div class="label">MINDFULLNESS MEDITATION<br>LIFE COACHING</div>
    <div></div><div><svg class="tick c-mental"><use href="#tick"/></svg></div><div></div><div></div><div></div><div></div><div><svg class="tick c-testing"><use href="#tick"/></svg></div></div>
  <div class="row alt" style="height:24px"><div class="label">HYPNOTHERAPHY<br>INNER CHILD HEALING</div>
    <div></div><div><svg class="tick c-mental"><use href="#tick"/></svg></div><div></div><div></div><div><svg class="tick c-sub"><use href="#tick"/></svg></div><div></div><div></div></div>
  <div class="row alt" style="height:24px;border-bottom:none"><div class="label">NLP<br>TIMELINE THERAPHY</div>
    <div></div><div><svg class="tick c-mental"><use href="#tick"/></svg></div><div></div><div></div><div><svg class="tick c-sub"><use href="#tick"/></svg></div><div></div><div><svg class="tick c-testing"><use href="#tick"/></svg></div></div>
</section>

<footer>
  <div class="partner"><span class="dot"></span><span class="name">lumenwell</span></div>
  <div class="site">WWW.LUMENWELL.COM.AU</div>

  <span class="notes-col" style="left:270px"></span>
  <span class="notes-col" style="left:492px"></span>
  <span class="notes-col" style="left:714px"></span>
  <span class="notes-col" style="left:938px"></span>

  <div class="notes n1">
    <div><h3 style="color:var(--physical)">PHYSICAL</h3><p>Most modalities, including a western medicine, focus on and treat the physical body only. The KRV process enables you to engage in healing your own body during the session. There is no muscle testing, no hands-on healing and no herbal remedies or medicines.</p></div>
  </div>
  <div class="notes n2">
    <div><h3 style="color:var(--mental)">MENTAL</h3><p>KRV enables you to use your own consciousness to self-heal. We don't give you advice or coaching, we allow your mind to heal itself.</p></div>
    <div><h3 style="color:var(--emotional)">EMOTIONAL</h3><p>KRV is the only modality that engages your emotions on a physical level. Emotions get stuck in your body and can cause illness over time if left unchecked. KRV enables you to experience fast and powerful emotional releasing.</p></div>
  </div>
  <div class="notes n3">
    <div><h3 style="color:var(--energetic)">ENERGETIC</h3><p>Most modalities try to move the energy in your body for you. KRV enables and empowers you to do it yourself.</p></div>
    <div><h3 style="color:#efd93a">SUBCONSCIOUS</h3><p>Some modalities, like Kinesiology, access your subconscious through muscle testing. KRV empowers you to access your own subconscious and heal it yourself.</p></div>
  </div>
  <div class="notes n4">
    <div><h3 style="color:var(--superconscious)">SUPERCONSIOUS</h3><p>KRV is the only modality that enables you to access and heal your superconscious mind yourself.</p></div>
    <div><h3 style="color:var(--testing)">BEFORE &amp; AFTER TESTING</h3><p>KRV is the only modality that enables you to provide before and after results, which are documented by us, and analysed by you with our help.</p></div>
  </div>
</footer>
</body>
</html>
```